Pell Haven Branding for Contracts and Customer facing documents

We are hoping to create a themed branding for our company. We would like to leverage this across our contracts, documents, and all client information and proposals. www.BuildWithPell.com is our website. We are selling high end custom homes. We am intending to use this template for a Lead Magnet and other marketing.

Target Market(s)

Luxury Custom Home Buyers

Industry/Entity Type

Residential Construction

Other font styles liked:
• You may choose, We want to be elegant but very legible and professional

Colors
0054AA
0677BA
7BADD7
CADEEF
E8F1F8

```html
<!DOCTYPE html>
<html lang="en">
<head>
<meta charset="utf-8">
<title>Pell Haven – Step 3 Drainfield Exploration</title>
<link href="https://fonts.googleapis.com/css2?family=Montserrat:wght@300;400;600;700&display=swap" rel="stylesheet">
<style>
  :root {
    --navy: #21405c;
    --gold: #d8b46c;
    --ink: #2b2b2b;
    --stripe-stone: #dcdad0;
    --stripe-blue: #e3ecf4;
    --paper: #ffffff;
    --panel: #fdfdfd;
    --edge: #c9c9c9;
    --photo-tone: #c4bcab;
  }
  * { margin: 0; padding: 0; box-sizing: border-box; }
  html, body { width: 928px; height: 1200px; overflow: hidden; background: var(--paper); }
  body { font-family: "Montserrat", Arial, sans-serif; color: var(--ink); }
  .page { position: relative; width: 928px; height: 1200px; border: 1px solid var(--edge); background: var(--paper); overflow: hidden; }
  .backdrop { position: absolute; inset: 0; }
  .panel { position: absolute; left: 85px; top: 214px; width: 780px; height: 876px; background: var(--panel); }

  .step-tab { position: absolute; left: 85px; top: 136px; width: 256px; height: 50px; background: var(--navy); color: #fff; font-weight: 700; font-size: 27px; letter-spacing: 0.5px; display: flex; align-items: center; padding-left: 27px; }
  .step-flourish { display: inline-block; width: 76px; height: 10px; margin-left: 35px; border-radius: 5px; background: linear-gradient(90deg, #6f8aa4, #a9bccd); }
  .step-accent { position: absolute; left: 341px; top: 118px; width: 88px; height: 17px; background: var(--gold); }
  .step-title { position: absolute; right: 74px; top: 144px; font-weight: 700; font-size: 27.5px; color: var(--navy); letter-spacing: 0.6px; }
  .rule { position: absolute; left: 85px; top: 211px; width: 777px; height: 2px; background: var(--gold); }

  .body-copy { font-weight: 300; font-size: 17.5px; line-height: 24px; letter-spacing: 0.7px; }
  .intro { position: absolute; left: 138px; top: 233px; width: 300px; }
  .intro strong { font-weight: 700; }
  .services { position: absolute; left: 133px; top: 442px; list-style: none; }
  .services li { display: flex; align-items: center; height: 27.3px; font-weight: 300; font-size: 17.5px; letter-spacing: 0.7px; }
  .bullet-mark { width: 23px; height: 11px; border-radius: 6px; background: var(--gold); margin-right: 25px; }

  .site-photo { position: absolute; left: 490px; top: 235px; width: 372px; height: 308px; background: var(--photo-tone); }

  .note { position: absolute; left: 138px; top: 596px; width: 700px; }
  .fee-box { position: absolute; left: 126px; top: 728px; width: 380px; height: 39px; border: 1px solid var(--gold); border-radius: 10px; display: flex; align-items: center; padding-left: 9px; font-size: 17.5px; letter-spacing: 0.3px; font-weight: 700; color: #1f1f1f; }
  .authorize { position: absolute; left: 138px; top: 773px; width: 690px; line-height: 22px; letter-spacing: 0.9px; }

  .signature-box { position: absolute; left: 126px; top: 915px; width: 703px; height: 145px; border: 1px solid var(--gold); border-radius: 10px; }
  .sig-row { position: absolute; left: 20px; right: 18px; display: flex; align-items: flex-end; font-weight: 300; font-size: 17.5px; letter-spacing: 0.5px; }
  .sig-label { width: 218px; }
  .leader { flex: none; border-bottom: 2px dotted #555; height: 1px; margin-bottom: 5px; }
  .leader.name { width: 252px; }
  .leader.date { width: 135px; }
  .sig-date { margin: 0 5px; }

  .footer-band { position: absolute; left: 85px; top: 1090px; width: 780px; height: 19px; background: var(--gold); }
  .footer { position: absolute; left: 85px; right: 63px; top: 1127px; display: flex; justify-content: space-between; font-weight: 400; font-size: 15.5px; letter-spacing: 1.3px; color: #3a3a3a; }
</style>
</head>
<body>
<div class="page">
  <svg class="backdrop" width="928" height="1200" viewBox="0 0 928 1200" aria-hidden="true">
    <defs>
      <linearGradient id="wash" x1="0" y1="0" x2="1" y2="1">
        <stop offset="0" stop-color="#d6e2ee"/>
        <stop offset="1" stop-color="#ffffff" stop-opacity="0"/>
      </linearGradient>
    </defs>
    <polygon points="0,250 220,0 660,0 0,800" fill="url(#wash)" opacity="0.7"/>
    <polygon points="0,240 200,0 250,0 0,290" fill="var(--stripe-stone)"/>
    <polygon points="110,100 165,100 110,170" fill="var(--stripe-stone)"/>
    <polygon points="128,100 210,0 245,0 162,100" fill="var(--stripe-stone)"/>
    <polygon points="195,210 370,0 380,0 205,210" fill="var(--stripe-stone)"/>
    <polygon points="258,136 370,0 376,0 264,136" fill="var(--stripe-stone)"/>
    <polygon points="0,420 85,315 85,330 0,430" fill="var(--stripe-blue)"/>
    <polygon points="928,960 928,1200 720,1200" fill="var(--stripe-blue)" opacity="0.6"/>
  </svg>

  <div class="panel"></div>

  <div class="step-accent"></div>
  <div class="step-tab">STEP 3 <span class="step-flourish" role="img" aria-label="Decorative flourish"></span></div>
  <h1 class="step-title">DRAINFIELD EXPLORATION</h1>
  <div class="rule"></div>

  <p class="intro body-copy">The third critical step in the process will give Pell Haven the approval to identify issues and any additional up front costs so we can plan accordingly and project an accurate budget number. The fee of <strong>$4,500.00</strong> will include the following:</p>

  <ul class="services">
    <li><span class="bullet-mark" role="img" aria-label="Bullet ornament"></span>Backhoe/Excavation Service</li>
    <li><span class="bullet-mark" role="img" aria-label="Bullet ornament"></span>Soil Evaluation</li>
    <li><span class="bullet-mark" role="img" aria-label="Bullet ornament"></span>Preliminary Surveying</li>
    <li><span class="bullet-mark" role="img" aria-label="Bullet ornament"></span>Drainfield Design</li>
  </ul>

  <div class="site-photo" role="img" aria-label="Photo of an excavator on a cleared home site"></div>

  <p class="note body-copy">Please note, that some of these services will not be necessary prior to contract and are based on the location of your home site and individual county guidelines. This fee paid up front is typically included in your overall budget number and will be adjusted on the final budget.</p>

  <div class="fee-box">Drainfield Exploration Fee: $4,500.00</div>

  <p class="authorize body-copy">By Signing below and paying the appropriate fees, you agree to the terms and authorize Pell Haven to proceed with the following services on your new home. In addition, you understand that no work will commence until all signatures are completed and payment is received in full.</p>

  <div class="signature-box">
    <div class="sig-row" style="top:22px"><span class="sig-label">Customer Signature(s):</span><span class="leader name"></span><span class="sig-date">Date:</span><span class="leader date"></span></div>
    <div class="sig-row" style="top:66px"><span class="sig-label"></span><span class="leader name"></span><span class="sig-date">Date:</span><span class="leader date"></span></div>
    <div class="sig-row" style="top:110px"><span class="sig-label">Pell Haven, LLC.:</span><span class="leader name"></span><span class="sig-date">Date:</span><span class="leader date"></span></div>
  </div>

  <div class="footer-band"></div>
  <div class="footer"><span>PELL HAVEN CUSTOM HOMES</span><span>4</span></div>
</div>
</body>
</html>
```